Social Media Designs for Pet Insurance Website

We are seeking the following
Twitter Background and Header Image
Facebook Cover
Google Plus Cover (1080×608)

All designs must comply with platform requirements with regard to size and other requirements (such as the Facebook text regulations).

The overriding requirement is for all 3 designs to be CONSISTENT with our website which can be found at www.critter-cover-reviews.co.uk.

We would like the five colours from the menu boxes beneath the header on our home page to be incorporated into the designs.

The photo of the dog and cat which is used in our header should be incorporated within the design.

We have attached the photo file and our logo file.

We will want to use the twitter margins to display additional information about the website which we will supply at a later stage.

You are free to amend the colours in the logo to suit the design if you wish.

All 3 designs must contain our strap line which is "Helping UK pet owners make the right pet insurance choice" and also this list
"Keep in touch
Join the discussion
Contribute your experiences"
Updates

Have just added the copy for the left hand margin on the twitter background as a new attachment to the brief.   One idea might be to display the text in boxes to mimic the menu boxes on our home page.   Just an idea though  .. very happy to see other ideas.

Reason: Unfortunately I have been called away from the office for the last couple of days so have been unable to provide the feedback etc. I have therefore decided to extend the deadline by a day.

Target Market(s)

Most importantly the designs should have the same look as feel as the website..www.critter-cover-reviews.co.uk

Industry/Entity Type

Pet

Requirements
Must have
• See brief above
Nice to have
• See brief above
Should not have
• See brief above

```html
<!DOCTYPE html>
<html lang="en">
<head>
<meta charset="utf-8">
<title>Critter Cover Reviews UK – Header</title>
<link href="https://fonts.googleapis.com/css2?family=Open+Sans:wght@600;700&display=swap" rel="stylesheet">
<style>
  :root {
    --leaf-deep: #5a8a24;
    --leaf-mid: #84b33c;
    --leaf-light: #b9d88a;
    --mist-pale: #d9e2cf;
    --ink-white: #ffffff;
    --band-dark: rgba(40, 40, 40, 0.72);
    --mark-dark: #1f2a36;
  }
  * { margin: 0; padding: 0; box-sizing: border-box; }
  html, body {
    width: 1200px;
    height: 600px;
    overflow: hidden;
    background: #ffffff;
  }
  .header-canvas {
    position: relative;
    width: 1200px;
    height: 600px;
    overflow: hidden;
    font-family: "Open Sans", Arial, sans-serif;
    color: var(--ink-white);
  }
  .scene-photo {
    position: absolute;
    inset: 0;
    background: linear-gradient(90deg, var(--leaf-deep) 0%, var(--leaf-mid) 40%, var(--leaf-light) 68%, var(--mist-pale) 100%);
  }
  .brand-square {
    position: absolute;
    left: 512px;
    top: 46px;
    width: 176px;
    height: 180px;
    background: var(--mark-dark);
    border: 8px solid var(--ink-white);
    border-radius: 6px;
    box-shadow: 0 4px 14px rgba(0, 0, 0, 0.35);
  }
  .brand-name {
    position: absolute;
    left: 0;
    right: 0;
    top: 252px;
    text-align: center;
    font-weight: 700;
    font-size: 32px;
    line-height: 48px;
    letter-spacing: 0.5px;
    text-transform: uppercase;
    text-shadow: 0 1px 4px rgba(0, 0, 0, 0.45);
  }
  .brand-handle {
    position: absolute;
    left: 0;
    right: 0;
    top: 352px;
    text-align: center;
    font-weight: 600;
    font-size: 29px;
    text-shadow: 0 1px 4px rgba(0, 0, 0, 0.45);
  }
  .message-band {
    position: absolute;
    left: 88px;
    top: 415px;
    width: 1024px;
    height: 139px;
    background: var(--band-dark);
    border-radius: 6px;
    display: flex;
    flex-direction: column;
    justify-content: center;
    align-items: center;
    gap: 20px;
  }
  .strap-line {
    font-weight: 700;
    font-size: 31px;
  }
  .action-list {
    list-style: none;
    display: flex;
    gap: 52px;
    font-weight: 600;
    font-size: 25px;
  }
  .action-list li::before {
    content: "»";
    font-weight: 700;
    margin-right: 10px;
  }
</style>
</head>
<body>
  <main class="header-canvas">
    <div class="scene-photo" role="img" aria-label="Header photo of a tortoise and a cat against a soft green garden background"></div>

    <div class="brand-square"></div>
    <h1 class="brand-name">Critter Cover<br>Reviews UK</h1>
    <p class="brand-handle">@crittercover</p>

    <section class="message-band">
      <p class="strap-line">Helping UK pet owners make the right pet insurance choice</p>
      <ul class="action-list">
        <li>Keep in touch</li>
        <li>Join the discussion</li>
        <li>Contribute your experiences</li>
      </ul>
    </section>
  </main>
</body>
</html>
```